ultra-minimalist business card

front (black background, matte):

tarik b. hosseny
writer | photographer
get@tarikhosseny.com

back (white background, matte):

a picture speaks a thousand words;
a word draws a thousand pictures.

www.tarikhosseny.com

all text should be small (white or silver - as long as it shows against the black - on the front; black or gray - as long as it shows against the white - on the back).

feel free to get creative in terms of arrangement, alignment, and font type, but remember, the overall style is minimalist, so nothing too fancy, please.

thanks.

```html
<!DOCTYPE html>
<html lang="en">
<head>
<meta charset="utf-8">
<title>tarik b. hosseny — business card</title>
<link href="https://fonts.googleapis.com/css2?family=Oswald:wght@300;400&display=swap" rel="stylesheet">
<style>
  :root {
    --backdrop: #8a8a8a;
    --card-black: #231f20;
    --card-white: #ffffff;
    --portrait-tone-light: #b3b4b6;
    --portrait-tone-dark: #9c9d9f;
    --silver-text: #c9cacc;
    --rule: #bfc0c2;
    --gray-text: #8c8d8f;
    --shadow: rgba(0, 0, 0, 0.35);
  }
  * { box-sizing: border-box; margin: 0; padding: 0; }
  html, body {
    width: 1200px;
    height: 1200px;
    overflow: hidden;
    background: var(--backdrop);
    font-family: "Oswald", "Arial Narrow", sans-serif;
    font-weight: 300;
  }
  .card {
    position: absolute;
    left: 246px;
    width: 710px;
    height: 402px;
    overflow: hidden;
    box-shadow: 0 4px 10px var(--shadow);
  }
  .card--front { top: 156px; background: var(--card-black); }
  .card--back  { top: 641px; background: var(--card-white); }

  .portrait {
    position: absolute;
    left: 0;
    top: 40px;
    width: 272px;
    height: 362px;
    background: linear-gradient(160deg, var(--portrait-tone-light), var(--portrait-tone-dark));
  }

  .front-text { position: absolute; left: 346px; color: var(--silver-text); white-space: nowrap; }
  .holder-name { top: 224px; font-size: 24px; line-height: 30px; letter-spacing: 1.6px; }
  .holder-role { top: 260px; font-size: 15px; line-height: 20px; letter-spacing: 1.65px; }
  .holder-email { top: 312px; font-size: 15px; line-height: 20px; letter-spacing: 1.85px; }
  .divider {
    position: absolute;
    left: 272px;
    right: 0;
    top: 297px;
    height: 1px;
    background: var(--rule);
  }

  .motto {
    position: absolute;
    left: 188px;
    top: 148px;
    font-size: 27px;
    line-height: 43px;
    color: var(--gray-text);
    letter-spacing: 1.75px;
    white-space: nowrap;
  }
  .website {
    position: absolute;
    left: 274px;
    top: 336px;
    font-size: 14px;
    line-height: 20px;
    color: var(--gray-text);
    letter-spacing: 1.9px;
    white-space: nowrap;
  }
</style>
</head>
<body>
  <section class="card card--front">
    <div class="portrait" role="img" aria-label="Area for the card holder's silver two-tone portrait illustration"></div>
    <p class="front-text holder-name">tarik b. hosseny</p>
    <p class="front-text holder-role">writer&nbsp; |&nbsp; photographer</p>
    <div class="divider"></div>
    <p class="front-text holder-email">get@tarikhosseny.com</p>
  </section>

  <section class="card card--back">
    <p class="motto">a picture speaks a thousand words;<br>a word draws a thousand pictures.</p>
    <p class="website">www.tarikhosseny.com</p>
  </section>
</body>
</html>
```